WordPress WEB DESIGN & CODING for www.quelbrix-aerial.com Wireless Tower Contruction

WEB DESIGN & CODING for www.quelbrix-aerial.com
Wireless Tower Contruction Industry

SLOGAN: SERVICE AT A HIGHER LEVEL

Brannock Spires LLC has been in business since 2014 with combined professional Team experience of over 40 years.

Our Team is composed of long-time industry professionals in every aspect of the wireless telecommunications and commercial construction industries, including project management and site acquisition.

Brannock Spires specializes in providing tower installation services for the Wireless Telecommunications in the Southeastern of the United States.

Our key services are Wireless Tower Construction, Installation & Maintenance

Site audits and Tower mapping
Mount swaps and Modifications
Hardline & Jumper Installation
Antenna & Radio Install, Decom, Testing and Maintenance
Tower Lighting Installation & Testing
Fiber / Sweep / RET/ PIM Testing
Small Cells
Civil installation (concrete/steel platforms/electrical)
____________________________________________________________________

we need a clean yet vibrant, energetic website design that will convey our tower installation work to the fullest... It should use the navy and green colors of our logo and it must be mobile friendly and coded for both Android & IOS;
the site structure:
HOME
ABOUT
SERVICES
CONTRACT
CAREERS
GALLERY

I also attach a few pics we bought on shutterstock so these can be used if needed as we own them...

Target Market(s)

Client: large companies looking for general contractor or installation contractor in the market

Industry/Entity Type

Wireless Communication

Coding

Coded - Design and coding required

Number of Pages Required

4 page

Font styles to use
Sans Serif

Colors
0555a3
00a990
ffffff

Requirements
Must have
• Wordpress - must be both desktop mobile friendly and mobile is the key -
• should open swiftly on both Android & iOS
• See power point file with presentation about the company; page 5 is our keyservices but other contents can be used too
Nice to have
• panorama pics changing from the height/tower view showing the full overview, could be a slideshow or a short video...
Should not have
• flash animation does not work on iOS so this should be avoided.

```html
<!DOCTYPE html>
<html lang="en">
<head>
<meta charset="utf-8">
<title>Brannock Spires — Wireless Tower Construction</title>
<link href="https://fonts.googleapis.com/css2?family=Poppins:wght@400;500;600;700;800&family=Open+Sans:wght@400;600&display=swap" rel="stylesheet">
<style>
:root{
  --navy:#0555a3;
  --navy-deep:#03447f;
  --navy-darker:#02376a;
  --green:#00a990;
  --white:#ffffff;
  --ink:#1d2733;
  --muted:#7a8591;
  --line:#e3e8ee;
  --soft:#f5f7fa;
  --star:#f3b81b;
}
*{box-sizing:border-box;margin:0;padding:0}
html,body{width:1200px;height:2960px;overflow:hidden}
body{font-family:'Open Sans',sans-serif;color:var(--ink);background:var(--white);position:relative}
h1,h2,h3,h4,.brand,.btn,.nav a,.eyebrow{font-family:'Poppins',sans-serif}
section,header,footer,nav{position:absolute;left:0;width:1200px}

/* top bar */
.topbar{top:0;height:88px;background:var(--white);z-index:3}
.brand{position:absolute;left:160px;top:26px;display:flex;align-items:center;gap:10px;font-weight:700;font-size:24px;color:var(--navy)}
.brand .dot{width:14px;height:14px;background:var(--green)}
.contact-items{position:absolute;left:450px;top:26px;display:flex;gap:46px}
.contact-item{display:flex;align-items:center;gap:10px;font-size:11px;color:var(--muted);line-height:1.35;white-space:nowrap}
.contact-item strong{display:block;color:var(--ink);font-size:12px}
.contact-item .ico{width:32px;height:32px;border-radius:50%;background:var(--navy);display:flex;align-items:center;justify-content:center;flex:none}
.nav{top:88px;height:36px;background:var(--navy);z-index:4}
.nav ul{list-style:none;display:flex;gap:28px;position:absolute;left:160px;top:0;height:36px;align-items:center}
.nav a{color:var(--white);font-size:11px;font-weight:600;text-decoration:none;letter-spacing:.5px}
.nav .cta{position:absolute;right:160px;top:-6px;height:42px;width:140px;background:var(--green);color:var(--white);font-family:'Poppins',sans-serif;font-size:11px;font-weight:600;display:flex;align-items:center;justify-content:center;letter-spacing:.5px}

/* hero */
.hero{top:124px;height:396px;background:linear-gradient(180deg,#cfd3d8 0%,#eef0f2 55%,#bfc4ca 100%)}
.hero .center{position:absolute;left:0;right:0;top:112px;text-align:center}
.hero .hero-name{font-family:'Poppins',sans-serif;font-weight:700;font-size:52px;color:var(--navy);letter-spacing:-.5px}
.hero .slogan{font-family:'Poppins',sans-serif;font-weight:700;font-style:italic;font-size:24px;color:var(--green);margin-top:2px}
.btn{display:inline-block;background:var(--navy);color:var(--white);font-size:10px;font-weight:600;padding:9px 22px;letter-spacing:.6px}
.hero .btn{margin-top:22px}
.dots{position:absolute;left:0;right:0;bottom:24px;display:flex;justify-content:center;gap:8px}
.dots span{width:9px;height:9px;border-radius:50%;background:#fff;opacity:.7}
.dots span.on{background:var(--navy);opacity:1}

/* about */
.about{top:520px;height:340px}
.about .media{position:absolute;left:220px;top:40px;width:360px;height:250px;background:linear-gradient(160deg,#d9dde2,#8d959e)}
.play{position:absolute;left:155px;top:100px;width:50px;height:50px;border-radius:50%;background:var(--navy);display:flex;align-items:center;justify-content:center}
.about .copy{position:absolute;left:620px;top:40px;width:380px}
.eyebrow{font-size:10px;font-weight:600;color:var(--green);letter-spacing:1px;text-transform:uppercase}
.about h2{font-size:26px;font-weight:700;color:var(--ink);margin:6px 0 12px}
.about h2::after{content:"";display:block;width:40px;height:3px;background:var(--green);margin-top:8px}
.about p{font-size:11px;line-height:1.7;color:var(--muted);margin-bottom:10px}
.about .sign{font-family:'Poppins',sans-serif;font-weight:700;font-size:14px;color:var(--navy);display:flex;align-items:center;gap:8px;margin-top:14px}
.about .sign i{width:10px;height:10px;background:var(--green);display:block}

/* services */
.services{top:860px;height:520px;background:var(--soft)}
.services .bg-left{position:absolute;left:0;top:60px;width:260px;height:440px;background:linear-gradient(180deg,#e6e9ed,#d4d9de);opacity:.8}
.services .workers{position:absolute;left:940px;top:200px;width:220px;height:290px;background:linear-gradient(180deg,#f2c230 0%,#2f5f93 55%,#1c3c63 100%)}
.section-head{text-align:center}
.section-head .eyebrow{display:block}
.section-head h2{font-size:28px;font-weight:700;color:var(--ink);margin-top:4px}
.section-head p{font-size:11px;color:var(--muted);margin-top:8px;line-height:1.6}
.services .section-head{position:absolute;left:0;right:0;top:40px}
.cards{position:absolute;left:210px;top:162px;width:720px;display:grid;grid-template-columns:repeat(4,1fr);gap:10px}
.card{background:var(--white);border:1px solid var(--line);height:132px;display:flex;flex-direction:column;align-items:center;justify-content:center;text-align:center;padding:0 12px}
.card svg{margin-bottom:12px}
.card h4{font-size:10px;font-weight:600;color:var(--ink);line-height:1.4;text-transform:uppercase}
.services .more{position:absolute;left:0;right:0;top:462px;text-align:center}
.services .more span{font-family:'Poppins',sans-serif;font-weight:700;font-size:12px;color:var(--navy);border:1px solid var(--navy);padding:8px 18px;display:inline-flex;align-items:center;gap:8px}
.services .more i{width:8px;height:8px;background:var(--green);display:block}

/* works */
.works{top:1380px;height:800px}
.works .section-head{position:absolute;left:0;right:0;top:40px}
.filters{position:absolute;left:0;right:0;top:120px;display:flex;justify-content:center;gap:8px}
.filters span{font-family:'Poppins',sans-serif;font-size:9px;font-weight:600;color:var(--ink);border:1px solid var(--line);padding:7px 14px;text-transform:uppercase}
.filters span.on{background:var(--navy);color:var(--white);border-color:var(--navy)}
.grid{position:absolute;left:0;top:180px;width:1200px;display:grid;grid-template-columns:repeat(3,400px);grid-auto-rows:280px}
.tile{position:relative}
.tile.t1{background:linear-gradient(160deg,#2a6fb8,#0b3f78)}
.tile.t2{background:linear-gradient(180deg,#3b6fb0,#a34b2a)}
.tile.t3{background:linear-gradient(180deg,#f4f6f8,#c9d2db)}
.tile.t4{background:linear-gradient(180deg,#7a9bbf,#3b5573)}
.tile.t5{background:linear-gradient(180deg,#3a8ad6,#a9cbeb)}
.tile.t6{background:linear-gradient(180deg,#6fa9df,#e8eff6)}
.tile .caption{position:absolute;left:0;right:0;bottom:0;background:rgba(5,85,163,.78);color:var(--white);font-family:'Poppins',sans-serif;font-weight:600;font-size:15px;line-height:1.4;padding:20px 30px}

/* testimonials */
.testimonials{top:2180px;height:400px}
.testimonials .section-head{position:absolute;left:0;right:0;top:44px}
.testimonials h2{line-height:1.25}
.quotes{position:absolute;left:220px;top:150px;width:760px;display:grid;grid-template-columns:1fr 1fr;gap:30px}
.quote{background:var(--soft);padding:22px 24px;height:170px}
.stars{color:var(--star);font-size:13px;letter-spacing:2px}
.quote p{font-size:10.5px;line-height:1.7;color:var(--muted);margin:10px 0 14px}
.quote h4{font-size:12px;font-weight:600;color:var(--ink)}
.quote small{font-size:10px;color:var(--muted)}

/* contact strip & footer */
.site-footer{top:2610px;height:350px;background:var(--navy)}
.strip{position:absolute;left:220px;top:2580px;width:760px;height:60px;background:var(--green);display:flex;align-items:center;justify-content:space-around;color:var(--white);z-index:2}
.strip .item{display:flex;align-items:center;gap:10px;font-size:10px;line-height:1.3}
.strip .item b{font-family:'Poppins',sans-serif;font-size:14px}
.strip .item.split b{margin-left:8px}
.foot-cols{position:absolute;left:160px;top:70px;width:880px;display:grid;grid-template-columns:260px 130px 220px 220px;gap:20px;color:var(--white)}
.foot-cols .brand{position:static;color:var(--white);font-size:20px}
.foot-cols p{font-size:10px;line-height:1.7;opacity:.85;margin-top:10px}
.foot-cols h4{font-size:12px;font-weight:600;margin-bottom:12px;text-transform:uppercase}
.foot-cols ul{list-style:none}
.foot-cols li{font-size:10px;line-height:2.1;opacity:.85;display:flex;align-items:center;gap:8px}
.foot-cols li::before{content:"";width:4px;height:4px;background:var(--green);display:block}
.foot-cols .touch li::before{display:none}
.newsletter-input{display:flex;margin-top:4px}
.newsletter-input span{flex:1;height:30px;background:var(--white);font-size:9px;color:var(--muted);padding:9px}
.newsletter-input b{width:34px;height:30px;background:var(--green)}
.socials{display:flex;gap:8px;margin-top:14px}
.socials i{width:24px;height:24px;border-radius:50%;border:1px solid rgba(255,255,255,.6);display:block}
.copyright{position:absolute;left:0;bottom:0;width:1200px;height:40px;background:var(--navy-darker);color:rgba(255,255,255,.75);font-size:10px;display:flex;align-items:center;justify-content:center}
</style>
</head>
<body>

<header class="topbar">
  <div class="brand"><span class="dot"></span>Brannock Spires</div>
  <div class="contact-items">
    <div class="contact-item"><span class="ico"><svg width="14" height="14" viewBox="0 0 24 24"><path fill="#fff" d="M6.6 10.8a15 15 0 0 0 6.6 6.6l2.2-2.2c.3-.3.7-.4 1-.2 1.1.4 2.3.6 3.6.6.6 0 1 .4 1 1V20c0 .6-.4 1-1 1A17 17 0 0 1 3 4c0-.6.4-1 1-1h3.5c.6 0 1 .4 1 1 0 1.3.2 2.5.6 3.6.1.3 0 .7-.2 1z"/></svg></span><span>Call Us<strong>+1 (555) 014-2290</strong></span></div>
    <div class="contact-item"><span class="ico"><svg width="14" height="14" viewBox="0 0 24 24"><path fill="#fff" d="M3 5h18v14H3z"/><path fill="none" stroke="#0555a3" stroke-width="2" d="M3 6l9 7 9-7"/></svg></span><span>Email Us<strong>info@quelbrix-aerial.com</strong></span></div>
    <div class="contact-item"><span class="ico"><svg width="14" height="14" viewBox="0 0 24 24"><circle cx="12" cy="12" r="9" fill="none" stroke="#fff" stroke-width="2"/><path d="M12 7v5l3 2" stroke="#fff" stroke-width="2" fill="none"/></svg></span><span>Working Hours<strong>Mon - Fri 8:00 - 17:00</strong></span></div>
  </div>
</header>

<nav class="nav">
  <ul>
    <li><a href="#">HOME</a></li>
    <li><a href="#">ABOUT</a></li>
    <li><a href="#">SERVICES ▾</a></li>
    <li><a href="#">CONTRACT</a></li>
    <li><a href="#">CAREERS</a></li>
    <li><a href="#">GALLERY</a></li>
  </ul>
  <div class="cta">CONTACT US</div>
</nav>

<section class="hero" role="img" aria-label="Black and white photo of telecom lattice towers against a pale sky">
  <div class="center">
    <div class="hero-name">Brannock Spires</div>
    <div class="slogan">SERVICE AT A HIGHER LEVEL</div>
    <span class="btn">CONTACT US</span>
  </div>
  <div class="dots"><span class="on"></span><span></span><span></span></div>
</section>

<section class="about">
  <div class="media" role="img" aria-label="Video still of a telecom tower climber at work">
    <div class="play"><svg width="16" height="18" viewBox="0 0 16 18"><path d="M2 1l13 8-13 8z" fill="#fff"/></svg></div>
  </div>
  <div class="copy">
    <span class="eyebrow">Welcome to Brannock Spires</span>
    <h2>ABOUT THE COMPANY</h2>
    <p>Brannock Spires LLC has been in business since 2014 with combined professional Team experience of over 40 years.</p>
    <p>Our Team is composed of long-time industry professionals in every aspect of the wireless telecommunications and commercial construction industries, including project management and site acquisition.</p>
    <div class="sign"><i></i>Brannock Spires</div>
  </div>
</section>

<section class="services">
  <div class="bg-left" role="img" aria-label="Faded photo of a tall lattice tower"></div>
  <div class="workers" role="img" aria-label="Photo of tower technicians in hard hats"></div>
  <div class="section-head">
    <span class="eyebrow">Our Services</span>
    <h2>WIRELESS TOWER CONSTRUCTION</h2>
    <p>Brannock Spires provides tower installation services for wireless telecommunications<br>across the Southeastern United States, from audits to maintenance.</p>
  </div>
  <div class="cards">
    <div class="card"><svg width="34" height="34" viewBox="0 0 34 34" fill="none" stroke="#0555a3" stroke-width="2"><path d="M17 4L9 30M17 4l8 26M12 20h10M11 25h12"/><circle cx="17" cy="4" r="2"/></svg><h4>Site audits and tower mapping</h4></div>
    <div class="card"><svg width="34" height="34" viewBox="0 0 34 34" fill="none" stroke="#0555a3" stroke-width="2"><rect x="6" y="8" width="8" height="18"/><rect x="20" y="8" width="8" height="18"/><path d="M14 14h6M18 11l3 3-3 3"/></svg><h4>Mount swaps and modifications</h4></div>
    <div class="card"><svg width="34" height="34" viewBox="0 0 34 34" fill="none" stroke="#0555a3" stroke-width="2"><path d="M5 10c8 0 8 14 16 14h8M5 18h6"/><circle cx="29" cy="24" r="2"/></svg><h4>Hardline &amp; jumper installation</h4></div>
    <div class="card"><svg width="34" height="34" viewBox="0 0 34 34" fill="none" stroke="#0555a3" stroke-width="2"><rect x="13" y="6" width="8" height="22"/><path d="M8 10a10 10 0 0 0 0 14M26 10a10 10 0 0 1 0 14"/></svg><h4>Antenna &amp; radio install, decom, testing and maintenance</h4></div>
    <div class="card"><svg width="34" height="34" viewBox="0 0 34 34" fill="none" stroke="#0555a3" stroke-width="2"><circle cx="17" cy="12" r="6"/><path d="M14 20h6v6h-6zM17 2v3M7 12H4M30 12h-3"/></svg><h4>Tower lighting installation &amp; testing</h4></div>
    <div class="card"><svg width="34" height="34" viewBox="0 0 34 34" fill="none" stroke="#0555a3" stroke-width="2"><path d="M5 26h24M8 22l5-8 5 5 6-10 3 4"/></svg><h4>Microwave installation, testing and maintenance</h4></div>
    <div class="card"><svg width="34" height="34" viewBox="0 0 34 34" fill="none" stroke="#0555a3" stroke-width="2"><path d="M4 17h6l3-7 4 14 3-7h10"/></svg><h4>Fiber / sweep / RET / PIM testing</h4></div>
    <div class="card"><svg width="34" height="34" viewBox="0 0 34 34" fill="none" stroke="#0555a3" stroke-width="2"><rect x="12" y="10" width="10" height="18" rx="2"/><path d="M9 8a11 11 0 0 1 16 0M6 5a15 15 0 0 1 22 0"/></svg><h4>Small cells</h4></div>
  </div>
  <div class="more"><span><i></i>VIEW ALL SERVICES</span></div>
</section>

<section class="works">
  <div class="section-head">
    <span class="eyebrow">Gallery</span>
    <h2>LET'S SEE OUR WORKS</h2>
  </div>
  <div class="filters">
    <span class="on">All</span><span>Site Audits</span><span>Mount Swaps</span><span>Jumper Installation</span><span>Antennas &amp; Radio Install</span><span>PIM Testing</span><span>Small Cells</span>
  </div>
  <div class="grid">
    <div class="tile t1" role="img" aria-label="Photo of antennas on a tower against blue sky"><div class="caption">Antenna &amp; Radio Install, Decom,<br>Testing and Maintenance</div></div>
    <div class="tile t2" role="img" aria-label="Photo looking up at a steel tower structure"></div>
    <div class="tile t3" role="img" aria-label="Photo of a red and white communication mast"></div>
    <div class="tile t4" role="img" aria-label="Photo of dish antennas mounted on a mast"></div>
    <div class="tile t5" role="img" aria-label="Photo of a lattice tower under a clear blue sky"></div>
    <div class="tile t6" role="img" aria-label="Photo of a cell tower top against clouds"></div>
  </div>
</section>

<section class="testimonials">
  <div class="section-head">
    <span class="eyebrow">Testimonials</span>
    <h2>TRUSTED BY THOUSAND OF<br>PEOPLE &amp; COMPANIES.</h2>
  </div>
  <div class="quotes">
    <div class="quote">
      <div class="stars">★★★★★</div>
      <p>The crew arrived on schedule, kept the site safe and clean, and finished our antenna swap ahead of plan. Clear reports and great communication from start to finish.</p>
      <h4>Harlan Mercer</h4><small>Tallowbrook</small>
    </div>
    <div class="quote">
      <div class="stars">★★★★★</div>
      <p>Professional tower work done right the first time. Their testing and documentation saved us weeks on the rollout, and we will keep them on every future project.</p>
      <h4>Dale Ortner</h4><small>Network Manager</small>
    </div>
  </div>
</section>

<div class="strip">
  <div class="item split"><svg width="20" height="20" viewBox="0 0 24 24"><path fill="#fff" d="M6.6 10.8a15 15 0 0 0 6.6 6.6l2.2-2.2c.3-.3.7-.4 1-.2 1.1.4 2.3.6 3.6.6.6 0 1 .4 1 1V20c0 .6-.4 1-1 1A17 17 0 0 1 3 4c0-.6.4-1 1-1h3.5c.6 0 1 .4 1 1 0 1.3.2 2.5.6 3.6.1.3 0 .7-.2 1z"/></svg><span>Call Now<br>For More Details</span><b>+1 (555) 014-2290</b></div>
  <div class="item split"><svg width="20" height="20" viewBox="0 0 24 24"><path fill="#fff" d="M3 5h18v14H3z"/><path fill="none" stroke="#00a990" stroke-width="2" d="M3 6l9 7 9-7"/></svg><span>Email Us</span><b>info@quelbrix-aerial.com</b></div>
</div>

<footer class="site-footer">
  <div class="foot-cols">
    <div>
      <div class="brand"><span class="dot"></span>Brannock Spires</div>
      <p>Brannock Spires LLC has been in business since 2014 with combined professional Team experience of over 40 years, serving wireless carriers across the Southeastern United States.</p>
    </div>
    <div>
      <h4>Quick Links</h4>
      <ul><li>Home</li><li>About</li><li>Services</li><li>Contract</li><li>Careers</li><li>Gallery</li></ul>
    </div>
    <div class="touch">
      <h4>Get In Touch</h4>
      <ul><li>2210 Ridgeline Way, Norvale, GA</li><li>+1 (555) 014-2290</li><li>info@quelbrix-aerial.com</li></ul>
    </div>
    <div>
      <h4>Newsletter</h4>
      <p style="margin-top:0;margin-bottom:8px">Subscribe for project news and company updates.</p>
      <div class="newsletter-input"><span>Your email address</span><b></b></div>
      <div class="socials"><i></i><i></i><i></i><i></i></div>
    </div>
  </div>
  <div class="copyright">Copyright © 2024 Brannock Spires. All Rights Reserved.</div>
</footer>

</body>
</html>
```